Copperleaf Grill
there is none
Copperleaf Grill -
Simple
Danielle Whitcomb
Proprietor
318 Ferrand Street New Orleans, LA 70119
dwhitcomb@copperleaf-eats.com
www.copperleaf-eats.com
Use the same font of Grill and New Orleans for information on card
Just put the logo and website on the back of the card

```html
<!DOCTYPE html>
<html lang="en">
<head>
<meta charset="utf-8">
<title>Copperleaf Grill – Business Card</title>
<link rel="stylesheet" href="https://fonts.googleapis.com/css2?family=Questrial&display=swap">
<style>
  :root {
    --page: #ffffff;
    --card-light: #f7f7f7;
    --card-dark: #e4e4e4;
    --wine: #7b2248;
    --wine-deep: #5e1636;
    --ink: #4a4a4a;
  }
  * { box-sizing: border-box; margin: 0; padding: 0; }
  html, body {
    width: 1200px; height: 338px; overflow: hidden;
    background: var(--page);
    font-family: "Questrial", "Century Gothic", sans-serif;
    color: var(--ink);
  }
  .sheet { position: relative; width: 1200px; height: 338px; }
  .card {
    position: absolute; top: 0; height: 338px;
    background: linear-gradient(160deg, var(--card-light) 0%, var(--card-light) 45%, var(--card-dark) 100%);
    box-shadow: 0 1px 4px rgba(0,0,0,0.18);
    overflow: hidden;
  }
  .card--front { left: 0; width: 590px; }
  .card--back { left: 610px; width: 590px; }
  .band {
    position: absolute; top: 0; bottom: 0; left: 0; width: 26px;
    background: linear-gradient(90deg, var(--wine-deep), var(--wine));
  }

  .brand {
    display: flex; align-items: center; gap: 10px;
    color: var(--wine); font-size: 38px; line-height: 1; white-space: nowrap;
  }
  .brand__dot { width: 14px; height: 14px; border-radius: 50%; background: var(--wine); }
  .card--front .brand { position: absolute; left: 48px; top: 64px; }
  .card--back .brand { position: absolute; left: 26px; right: 0; top: 140px; justify-content: center; }

  .person { position: absolute; left: 84px; top: 268px; }
  .person__name { color: var(--wine); font-size: 17px; }
  .person__role { font-size: 11.5px; margin-top: 3px; }

  .contact {
    position: absolute; left: 330px; top: 246px;
    font-size: 11.5px; line-height: 13.5px; list-style: none; white-space: nowrap;
  }
  .contact__label { color: var(--wine); }

  .website {
    position: absolute; left: 26px; right: 0; top: 198px;
    text-align: center; color: var(--wine); font-size: 13px;
  }
</style>
</head>
<body>
<main class="sheet">
  <section class="card card--front" aria-label="Card front">
    <div class="band"></div>
    <div class="brand"><span class="brand__dot"></span><span>Copperleaf Grill</span></div>
    <div class="person">
      <p class="person__name">Danielle Whitcomb</p>
      <p class="person__role">Proprietor</p>
    </div>
    <ul class="contact">
      <li>318 Ferrand Street</li>
      <li>New Orleans, LA 70119</li>
      <li><span class="contact__label">Phone :</span> 504.555.0142</li>
      <li><span class="contact__label">Cell :</span> 504.555.0187</li>
      <li><span class="contact__label">Email :</span> dwhitcomb@copperleaf-eats.com</li>
      <li><span class="contact__label">Web :</span> www.copperleaf-eats.com</li>
    </ul>
  </section>

  <section class="card card--back" aria-label="Card back">
    <div class="band"></div>
    <div class="brand"><span class="brand__dot"></span><span>Copperleaf Grill</span></div>
    <p class="website">www.copperleaf-eats.com</p>
  </section>
</main>
</body>
</html>
```